Bluestone Advisory & Mgmt - Professional Business Cards

Hi!

I am a Real Estate Developer and Construction Consultant.

I have a lot of inspiration from previous designs and would be open to using the attached Designs as a starting point. I would like to see these styles incorporated into your designs.

I really need professional business card to go with it that includes my important info.

Look forward to seeing your designs!.

Target Market(s)

My Target market are building owners, lawyers, consultants.

Industry/Entity Type

Real Estate Development

Contact Information for Business Card

My Name: Dorian Pelkey
My Title: Principle
Company Name: Bluestone Advisory & Mgmt, LLC
Address: 348 West 71st Street, 9th FL New York, NY 10010
Mobile: 917.806.3971
Website: bam-hvx.example

Font styles to use
Serif
Sans Serif

Colors

Designer to choose colors to be used in the design.

Requirements
Must have
• Must incorporate the logo attached or have new that looks similar.
• Must use professional font that will be seen and judged by wealthy land owners and developers.
• Must incorporate some of the color green.
Should not have
• Photo's or pictures of people or buildings of any kind.

```html
<!DOCTYPE html>
<html lang="en">
<head>
<meta charset="utf-8">
<title>Bluestone Advisory &amp; Mgmt – Business Cards</title>
<link href="https://fonts.googleapis.com/css2?family=Raleway:wght@500&family=Roboto:wght@300;500&display=swap" rel="stylesheet">
<style>
  :root {
    --backdrop: #e4e4e4;
    --card: #ffffff;
    --green: #4cb77b;
    --grey: #9a9391;
    --grey-light: #a7a7a7;
    --rule: #d6d6d6;
  }
  * { box-sizing: border-box; margin: 0; padding: 0; }
  html, body {
    width: 1125px; height: 1200px; overflow: hidden;
    background: var(--backdrop);
  }
  .sheet { position: relative; width: 1125px; height: 1200px; }
  .card {
    position: absolute; left: 150px; width: 825px; height: 472px;
    background: var(--card); border-radius: 30px;
  }
  .card--front { top: 98px; }
  .card--back  { top: 631px; display: flex; align-items: center; justify-content: center; }

  .brand { display: flex; align-items: center; gap: 16px; }
  .brand__mark { flex: none; background: var(--green); }
  .brand__name {
    font-family: "Raleway", sans-serif; font-weight: 500; color: var(--green);
    line-height: 1.08;
  }
  .card--front .brand { position: absolute; left: 106px; top: 170px; width: 300px; }
  .card--front .brand__mark { width: 44px; height: 44px; }
  .card--front .brand__name { font-size: 30px; }
  .card--back .brand__mark { width: 60px; height: 60px; }
  .card--back .brand__name { font-size: 42px; }

  .divider {
    position: absolute; left: 412px; top: 142px; width: 1px; height: 187px;
    background: var(--rule);
  }
  .contact {
    position: absolute; left: 452px; top: 128px;
    font-family: "Roboto", sans-serif; font-weight: 300; color: var(--grey-light);
  }
  .contact__name { font-weight: 500; color: var(--green); font-size: 29px; line-height: 1.2; }
  .contact__title { font-size: 18px; margin-top: 2px; }
  .contact__lines { margin-top: 22px; font-size: 21px; line-height: 28px; }
  .contact__line { display: flex; align-items: center; gap: 7px; }
  .contact__line svg { flex: none; }
  .contact__address { margin-top: 18px; font-size: 21px; line-height: 27px; }
</style>
</head>
<body>
<main class="sheet">
  <section class="card card--front">
    <div class="brand">
      <span class="brand__mark"></span>
      <span class="brand__name">Bluestone Advisory &amp; Mgmt</span>
    </div>
    <div class="divider"></div>
    <div class="contact">
      <p class="contact__name">Dorian Pelkey</p>
      <p class="contact__title">Principle</p>
      <div class="contact__lines">
        <p class="contact__line">
          <svg width="16" height="22" viewBox="0 0 16 22" aria-hidden="true">
            <rect x="2" y="1.5" width="12" height="19" rx="2" fill="none" stroke="#4cb77b" stroke-width="2"/>
            <line x1="2" y1="16" x2="14" y2="16" stroke="#4cb77b" stroke-width="1.6"/>
          </svg>
          917.806.3971
        </p>
        <p class="contact__line">
          <svg width="18" height="18" viewBox="0 0 18 18" aria-hidden="true">
            <circle cx="9" cy="9" r="8" fill="#4cb77b"/>
            <ellipse cx="9" cy="9" rx="3.5" ry="8" fill="none" stroke="#fff" stroke-width="1.2"/>
            <line x1="1" y1="9" x2="17" y2="9" stroke="#fff" stroke-width="1.2"/>
          </svg>
          www.bam-hvx.example
        </p>
      </div>
      <p class="contact__address">348 West 71st Street<br>9th FL New York, NY 10010</p>
    </div>
  </section>

  <section class="card card--back">
    <div class="brand">
      <span class="brand__mark"></span>
      <span class="brand__name">Bluestone Advisory &amp; Mgmt</span>
    </div>
  </section>
</main>
</body>
</html>
```